Zielgruppe
Einzelnfirmen, Arbeitsgruppen und KMU im Dienstleistungssektor.
Aufgabenstellung
Vorweg: Dem Auftrag folgen weitere Teilaufträge an den Gewinner, natürlich gegen Bezahlung.
Für die bereits programmierte Webapplikation "tallo" wird ein Design benötigt. Tallo ähnelt den bereits bestehenden Zeiterfassungssystemen, soll sich aber anhand von Einfachheit, Speditivität und grafischer Eleganz von anderen abheben. Zudem sind Features geplant, die in anderen Systemen nicht oder nur mangelhaft implementiert sind.
Was benötigt wird:
1) Ein Log-In im Splashscreen-Style. Siehe Linkbox mit Beispiel. Das Login hebt sich vom Hauptdesign ab.
Elemente, die beim Login vorhanden sind: Email- und Passwortfeld, Passwort vergessen Link, Platz für das Logo des Accountinhabers (Firmenlogo o.ä).
Zum Logo des Accountinhabers: Wenn der Inhaber keines Hochgeladen hat soll das Login so angezeigt werden wie wenn kein Platz für ein Logo da wäre. Dies muss aber nicht separat nochmals als Design hochgeladen werden, es reicht mir eine Version mit einem Logo. Als Logo kann beispielsweise das Firmenlogo von ravelmark verwendet werden.
2) Das Hauptdesign, welches für die Webapplikation gilt. Also für alles andere ausser das Login. Hier ist beispielsweise die Navigation vorhanden und eine kleine Version vom tallo logo. In das Hauptdesign werden alle weiteren Inhalte der Applikation integriert (Projektliste, Zeiterfassung, Benutzer-Management, Statistiken, Abrechnungen, ...).
Für den Beispielinhalt hätte ich gern eine simple Liste/Tabelle, beispielsweise von Systembenutzern oder Projekten und kein Lorem Ipsum.
Für mich ist es relativ schwer, alles zu beschreiben, da ich von Anfang an bei tallo mitgearbeitet habe und dort mitten drin bin. Fragen sind also sehr willkommen und werden ausführlich beantwortet!

```html
<!DOCTYPE html>
<html lang="en">
<head>
<meta charset="utf-8">
<title>tallo – login</title>
<link rel="stylesheet" href="https://fonts.googleapis.com/css2?family=Arimo:wght@400;700&display=swap">
<style>
  :root {
    --bg-center: #2197e6;
    --bg-edge: #0070c4;
    --panel-top: #efefef;
    --panel-body: #ffffff;
    --panel-foot: #ececec;
    --rule: #d6d6d6;
    --text-main: #555555;
    --text-header: #4a4a4a;
    --link: #1a72c6;
    --field-border: #c9c9c9;
    --brand-orange: #f39200;
    --btn-blue-top: #2b8fe0;
    --btn-blue-bottom: #0a6bc6;
    --white: #ffffff;
  }
  * { box-sizing: border-box; margin: 0; padding: 0; }
  html, body {
    width: 1200px;
    height: 901px;
    overflow: hidden;
  }
  body {
    position: relative;
    font-family: "Arimo", Arial, sans-serif;
    background: radial-gradient(ellipse 600px 520px at 600px 470px, var(--bg-center) 0%, #1586d8 55%, var(--bg-edge) 100%);
  }
  .app-brand {
    position: absolute;
    left: 540px;
    top: 126px;
    width: 140px;
    text-align: center;
    color: var(--white);
  }
  .app-brand__name {
    display: block;
    font-size: 40px;
    line-height: 44px;
    font-weight: 400;
    letter-spacing: 0.5px;
  }
  .app-brand__tagline {
    display: block;
    font-size: 11px;
    line-height: 14px;
    border-top: 1px solid rgba(255,255,255,0.6);
    padding-top: 2px;
  }
  .login-panel {
    position: absolute;
    left: 293px;
    top: 226px;
    width: 618px;
    height: 424px;
    border-radius: 10px;
    overflow: hidden;
    background: linear-gradient(to bottom, var(--panel-top) 0%, var(--panel-body) 45%, var(--panel-body) 100%);
    box-shadow: 0 2px 8px rgba(0, 40, 90, 0.45);
  }
  .login-panel__title {
    position: absolute;
    left: 35px;
    top: 15px;
    font-size: 19px;
    font-weight: 400;
    color: var(--text-header);
  }
  .login-panel__rule {
    position: absolute;
    left: 24px;
    right: 24px;
    top: 48px;
    height: 1px;
    background: var(--rule);
  }
  .field-label {
    position: absolute;
    right: 417px;
    font-size: 20px;
    color: var(--text-main);
    text-align: right;
  }
  .field-label--email { top: 106px; }
  .field-label--password { top: 167px; }
  .field-input {
    position: absolute;
    left: 253px;
    width: 300px;
    height: 36px;
    border: 1px solid var(--field-border);
    border-top-color: #a9a9a9;
    background: var(--white);
    box-shadow: inset 0 1px 2px rgba(0,0,0,0.08);
  }
  .field-input--email { top: 99px; }
  .field-input--password { top: 160px; }
  .forgot-link {
    position: absolute;
    right: 65px;
    top: 207px;
    font-size: 16px;
    color: var(--link);
    text-decoration: none;
  }
  .owner-logo {
    position: absolute;
    left: 188px;
    top: 252px;
    display: flex;
    align-items: center;
    gap: 10px;
  }
  .owner-logo__mark {
    width: 22px;
    height: 22px;
    border-radius: 50%;
    background: var(--brand-orange);
  }
  .owner-logo__name {
    font-size: 42px;
    font-weight: 700;
    color: var(--brand-orange);
    line-height: 56px;
  }
  .login-panel__footer {
    position: absolute;
    left: 0;
    right: 0;
    bottom: 0;
    height: 62px;
    background: var(--panel-foot);
    border-top: 1px solid var(--rule);
  }
  .btn {
    position: absolute;
    top: 12px;
    height: 36px;
    border-radius: 5px;
    font-family: "Arimo", Arial, sans-serif;
    text-align: center;
    line-height: 34px;
  }
  .btn--reset {
    left: 287px;
    width: 155px;
    font-size: 17px;
    color: #666666;
    background: linear-gradient(to bottom, #ffffff, #ededed);
    border: 1px solid #cfcfcf;
  }
  .btn--login {
    left: 454px;
    width: 152px;
    font-size: 19px;
    font-weight: 700;
    color: var(--white);
    background: linear-gradient(to bottom, var(--btn-blue-top), var(--btn-blue-bottom));
    border: 1px solid #085fae;
  }
</style>
</head>
<body>
  <header class="app-brand">
    <span class="app-brand__name">tallo</span>
    <span class="app-brand__tagline">pure time management</span>
  </header>

  <main class="login-panel">
    <h1 class="login-panel__title">tallo - login panel</h1>
    <div class="login-panel__rule"></div>

    <label class="field-label field-label--email">E-Mail Adress:</label>
    <div class="field-input field-input--email"></div>

    <label class="field-label field-label--password">Password:</label>
    <div class="field-input field-input--password"></div>

    <a class="forgot-link" href="#">forgot your password?</a>

    <div class="owner-logo">
      <span class="owner-logo__mark"></span>
      <span class="owner-logo__name">ravelmark</span>
    </div>

    <footer class="login-panel__footer">
      <div class="btn btn--reset">Reset</div>
      <div class="btn btn--login">Login</div>
    </footer>
  </main>
</body>
</html>
```